wood grain ultrasonic essential oil aroma diffuser

Design a package that is simple but luxurious for the diffuser with my logo. My business is called “Gentle Ember Path”. The logo incorporates “Thoughts become things” the concept is positive thinking. I don’t particularly want the product featured as I have like to develop a uniform look for packaging and website and there are 2 different diffusers,

Target Market(s)

People interested in yoga, meditation, metaphysical aspects

Industry/Entity Type

Health And Wellness

Colors

Designer to choose colors to be used in the design.

Requirements
Must have
• Luxurious feel to packaging and alignment with the website

```html
<!DOCTYPE html>
<html lang="en">
<head>
<meta charset="utf-8">
<title>Gentle Ember Path – Ultrasonic Oil Diffuser Packaging</title>
<link rel="stylesheet" href="https://fonts.googleapis.com/css2?family=Open+Sans:wght@300;400;600&display=swap">
<style>
  :root{
    --stage:#ececec;
    --box-dark:#1d1b19;
    --box-deep:#121110;
    --teal:#0ba6be;
    --white:#ffffff;
    --wood-dark:#4a3a33;
    --wood-mid:#6b5549;
    --wood-light:#e9a552;
    --wood-amber:#c9782c;
  }
  *{box-sizing:border-box;margin:0;padding:0}
  html,body{width:1200px;height:780px;overflow:hidden}
  body{background:var(--stage);font-family:"Open Sans",sans-serif;color:var(--white);position:relative}

  .panel{position:absolute;overflow:hidden;background:linear-gradient(160deg,#2a2724 0%,var(--box-dark) 55%,var(--box-deep) 100%)}
  .panel--top{left:150px;top:30px;width:300px;height:225px}
  .panel--front{left:150px;top:255px;width:300px;height:420px}
  .panel--features{left:450px;top:255px;width:300px;height:420px;background:var(--box-deep)}
  .panel--info{left:750px;top:255px;width:300px;height:420px;background:linear-gradient(180deg,#1a1817,#0e0d0c)}

  .fill{position:absolute}
  .svg-layer{position:absolute;left:0;top:0}

  /* brand: name + one plain circle */
  .brand{position:absolute;display:flex;flex-direction:column;align-items:center;gap:6px}
  .brand__dot{width:34px;height:34px;border-radius:50%;background:var(--white)}
  .brand__name{font-size:10px;font-weight:400;color:var(--white);letter-spacing:.5px;white-space:nowrap}

  /* top panel */
  .top__photo{left:90px;top:60px;width:190px;height:165px;border-radius:50% 50% 0 0 / 70% 70% 0 0;background:radial-gradient(ellipse at 50% 30%,var(--wood-mid),var(--wood-dark) 70%)}
  .top__brand{left:40px;top:8px}
  .top__brand .brand__dot{width:26px;height:26px}
  .top__title{position:absolute;left:26px;top:50px;font-size:18px;font-weight:400;transform:rotate(-10deg);transform-origin:left top;white-space:nowrap}

  /* front panel */
  .front__room{left:0;top:0;width:300px;height:420px;background:linear-gradient(180deg,rgba(70,64,58,.35),rgba(20,18,16,0) 70%)}
  .front__tab{position:absolute;left:186px;top:0;width:66px;height:74px;background:var(--teal);display:flex;flex-direction:column;align-items:center;justify-content:center;gap:6px}
  .front__tab .brand__dot{width:24px;height:24px}
  .front__tab .brand__name{font-size:6.5px}
  .title{position:absolute;text-align:right;line-height:1}
  .title__main{display:block;font-weight:400;font-size:32px}
  .title__sub{display:block;font-weight:400;font-size:22px;margin-top:2px}
  .front__title{right:28px;top:92px}
  .front__photo{left:135px;top:170px;width:120px;height:230px;border-radius:48% 48% 40% 40% / 60% 60% 28% 28%;background:radial-gradient(ellipse at 40% 40%,var(--wood-mid),var(--wood-dark) 75%)}
  .benefits{position:absolute;left:14px;top:210px;list-style:none}
  .benefits li{font-size:16px;font-weight:400;line-height:1.4;display:flex;align-items:center;gap:6px;white-space:nowrap}
  .benefits svg{width:10px;height:10px}

  .specs{position:absolute;display:flex;gap:12px}
  .specs--column{left:262px;top:300px;flex-direction:column;gap:8px}
  .spec{display:flex;flex-direction:column;align-items:center;gap:2px;font-size:6px;line-height:1.2;color:var(--white);text-align:center;width:32px}
  .spec svg{width:18px;height:18px}

  /* features panel */
  .features__brand{left:44px;top:22px}
  .features__brand .brand__dot{width:48px;height:48px}
  .badge{position:absolute;left:18px;top:100px;width:52px;height:52px;border:2px solid var(--white);border-radius:50%;display:flex;align-items:center;justify-content:center;gap:1px}
  .badge__small{font-size:6px;line-height:1;writing-mode:vertical-rl;transform:rotate(180deg)}
  .badge__num{font-size:22px;font-weight:400;line-height:1}
  .badge__unit{font-size:8px;align-self:flex-end;margin-bottom:16px}
  .features__photo-back{left:55px;top:165px;width:110px;height:185px;border-radius:48% 48% 38% 38% / 60% 60% 28% 28%;background:radial-gradient(ellipse at 40% 40%,var(--wood-mid),var(--wood-dark) 75%)}
  .features__photo-front{left:100px;top:215px;width:110px;height:195px;border-radius:48% 48% 38% 38% / 60% 60% 28% 28%;background:radial-gradient(ellipse at 45% 40%,var(--wood-light),var(--wood-amber) 80%)}
  .callout{position:absolute;font-size:6px;color:var(--white);line-height:1.25;white-space:nowrap}
  .callout--fog{left:180px;top:172px}
  .callout--light{left:4px;top:236px}
  .callout--light-btn{left:8px;top:366px}
  .callout--mist{left:212px;top:380px}
  .vertical-name{position:absolute;left:250px;top:410px;transform:rotate(-90deg);transform-origin:left top;font-size:40px;font-weight:400;color:var(--teal);white-space:nowrap;line-height:1}

  /* info panel */
  .info__brand{left:175px;top:36px}
  .info__brand .brand__dot{width:44px;height:44px}
  .info__title{right:28px;top:112px}
  .info__title .title__main{font-size:28px}
  .info__title .title__sub{font-size:20px}
  .copy{position:absolute;left:14px;top:205px;width:272px;display:flex;gap:14px}
  .copy p{flex:1;font-size:7.4px;line-height:1.45;color:var(--white)}
  .specs--row{left:84px;top:320px}
  .specs--row .spec{width:40px;font-size:6.5px;color:var(--teal)}
  .specs--row .spec svg{width:26px;height:26px}
</style>
</head>
<body>

<section class="panel panel--top" aria-label="Box top">
  <div class="fill top__photo" role="img" aria-label="Dark wood grain diffuser seen from above"></div>
  <div class="brand top__brand"><span class="brand__dot"></span></div>
  <p class="top__title">Gentle Ember Path</p>
</section>

<section class="panel panel--front" aria-label="Box front">
  <div class="fill front__room" role="img" aria-label="Dimmed living room interior"></div>
  <svg class="svg-layer" width="300" height="420" viewBox="0 0 300 420" aria-hidden="true">
    <polygon points="0,198 300,198 300,290 0,290" fill="var(--teal)"/>
  </svg>
  <div class="front__tab">
    <span class="brand__dot"></span>
    <span class="brand__name">Gentle Ember Path</span>
  </div>
  <h1 class="title front__title">
    <span class="title__main">Ultrasonic</span>
    <span class="title__sub">Oil Diffuser</span>
  </h1>
  <div class="fill front__photo" role="img" aria-label="Dark wood grain tulip shaped diffuser with teal light ring"></div>
  <ul class="benefits">
    <li><svg viewBox="0 0 10 10"><path d="M1 9 L9 1" stroke="#fff" stroke-width="1.2"/></svg>Relaxing</li>
    <li><svg viewBox="0 0 10 10"><path d="M1 9 L9 1" stroke="#fff" stroke-width="1.2"/></svg>Quiet Sound</li>
    <li><svg viewBox="0 0 10 10"><path d="M1 9 L9 1" stroke="#fff" stroke-width="1.2"/></svg>Smooth Design</li>
  </ul>
  <div class="specs specs--column">
    <div class="spec"><svg viewBox="0 0 20 20"><rect x="3" y="2" width="14" height="16" rx="2" fill="none" stroke="var(--teal)" stroke-width="1.5"/><line x1="5" y1="8" x2="15" y2="8" stroke="var(--teal)" stroke-width="1.5"/></svg>350ml</div>
    <div class="spec"><svg viewBox="0 0 20 20"><path d="M3 17 L3 7 L10 3 L17 7 L17 17 Z" fill="none" stroke="var(--teal)" stroke-width="1.5"/><path d="M7 14 Q10 9 13 14" fill="none" stroke="var(--teal)" stroke-width="1.5"/></svg>Covering area<br>269-323<br>sq.ft</div>
    <div class="spec"><svg viewBox="0 0 20 20"><path d="M16 10 A6 6 0 1 1 13 4.8" fill="none" stroke="var(--teal)" stroke-width="1.5"/><path d="M11 3 L14 4.5 L12.5 7.5" fill="none" stroke="var(--teal)" stroke-width="1.5"/></svg>Cycle</div>
  </div>
</section>

<section class="panel panel--features" aria-label="Box side with product features">
  <div class="brand features__brand">
    <span class="brand__dot"></span>
    <span class="brand__name">Gentle Ember Path</span>
  </div>
  <div class="badge">
    <span class="badge__small">up to</span>
    <span class="badge__num">12</span>
    <span class="badge__unit">hr</span>
  </div>
  <div class="fill features__photo-back" role="img" aria-label="Dark wood grain diffuser"></div>
  <div class="fill features__photo-front" role="img" aria-label="Light wood grain diffuser with teal light ring"></div>
  <svg class="svg-layer" width="300" height="420" viewBox="0 0 300 420" aria-hidden="true">
    <g stroke="#fff" stroke-width=".8" fill="none">
      <polyline points="192,182 192,205 170,222"/>
      <polyline points="20,246 20,300 60,300"/>
      <polyline points="30,364 30,345 140,345"/>
      <polyline points="222,378 222,360 180,360"/>
    </g>
    <circle cx="60" cy="300" r="2" fill="#fff"/>
    <circle cx="140" cy="345" r="2" fill="#fff"/>
    <circle cx="180" cy="360" r="2" fill="#fff"/>
  </svg>
  <span class="callout callout--fog">Fog Outlet</span>
  <span class="callout callout--light">Ambience Light</span>
  <span class="callout callout--light-btn">Turn on Light<br>Button</span>
  <span class="callout callout--mist">Turn on Mist<br>Button</span>
  <span class="vertical-name">Gentle Ember Path</span>
</section>

<section class="panel panel--info" aria-label="Box side with product description">
  <div class="brand info__brand">
    <span class="brand__dot"></span>
    <span class="brand__name">Gentle Ember Path</span>
  </div>
  <h2 class="title info__title">
    <span class="title__main">Ultrasonic</span>
    <span class="title__sub">Oil Diffuser</span>
  </h2>
  <svg class="svg-layer" width="300" height="420" viewBox="0 0 300 420" aria-hidden="true">
    <polygon points="0,192 300,192 300,290 0,290" fill="var(--teal)"/>
  </svg>
  <div class="copy">
    <p>A calm mist of your favourite oils fills the room in minutes. Soft light and a near silent motor help you slow down for yoga, meditation or a quiet evening at home.</p>
    <p>Fill the tank with water, add a few drops of oil and press the mist button. Choose a light colour, then let the timer switch the diffuser off when the water runs low.</p>
  </div>
  <div class="specs specs--row">
    <div class="spec"><svg viewBox="0 0 20 20"><rect x="3" y="2" width="14" height="16" rx="2" fill="none" stroke="var(--teal)" stroke-width="1.5"/><line x1="5" y1="8" x2="15" y2="8" stroke="var(--teal)" stroke-width="1.5"/></svg>350ml</div>
    <div class="spec"><svg viewBox="0 0 20 20"><path d="M3 17 L3 7 L10 3 L17 7 L17 17 Z" fill="none" stroke="var(--teal)" stroke-width="1.5"/><path d="M7 14 Q10 9 13 14" fill="none" stroke="var(--teal)" stroke-width="1.5"/></svg>Covering area 269-323sq.ft</div>
    <div class="spec"><svg viewBox="0 0 20 20"><path d="M16 10 A6 6 0 1 1 13 4.8" fill="none" stroke="var(--teal)" stroke-width="1.5"/><path d="M11 3 L14 4.5 L12.5 7.5" fill="none" stroke="var(--teal)" stroke-width="1.5"/></svg>Cycle</div>
  </div>
</section>

</body>
</html>
```